One-Page Flat Design for SEO Company [2 DAYS]

We need a one-page flat design for our SEO company. Our current website is http://www.rankloft.com/. We are looking to completely re-design the site using new flat design techniques.
Below are some examples of the type of style we're going after:
http://quormel.com/
http://tobyrand.co.uk/
https://pentaly.co/
http://milesporter.me/
As you can see- flat, clean, minimal. It is very important you follow this type of style.
For colour scheme, you may use one of the pre-made colour palettes from here:
http://www.vornacle.com/blog/inspiration/24-flat-designs-with-compelling-color-palettes
I've attached a wireframe to be followed.
Hi,

```html
<!DOCTYPE html>
<html lang="en">
<head>
<meta charset="utf-8">
<title>Rank Loft — One-Page SEO Site</title>
<link rel="stylesheet" href="https://fonts.googleapis.com/css2?family=Antonio:wght@300;400&family=PT+Sans:wght@400;700&family=Raleway:ital,wght@1,300&display=swap">
<style>
:root{
  --charcoal:#2e2a2b;
  --hero-top:#363233;
  --hero-bottom:#5d5a5b;
  --yellow:#f9cd3a;
  --teal:#1f8b82;
  --salmon:#f26b69;
  --royal:#233d99;
  --cyan:#3ee0f0;
  --sky:#3ab0e8;
  --chevron:#b8952f;
  --grey:#9a9a9a;
  --card-grey:#8a8a8a;
  --white:#ffffff;
  --ink:#2b2b2b;
  --display:"Antonio",sans-serif;
  --body:"PT Sans",sans-serif;
}
*{box-sizing:border-box;margin:0;padding:0}
html,body{width:1200px;height:1000px;overflow:hidden;background:var(--white)}
.canvas{position:relative;width:1200px;height:1000px;font-family:var(--body);color:var(--white)}
.panel{position:absolute;overflow:hidden}
.abs{position:absolute}
.center{text-align:center}
.display{font-family:var(--display);font-weight:300;letter-spacing:.5px;line-height:1}

/* hero */
.hero{left:17px;top:18px;width:583px;height:322px;background:linear-gradient(var(--hero-top) 0%,var(--hero-top) 45%,var(--hero-bottom) 100%)}
.nav{left:0;top:0;width:100%;height:33px;background:var(--charcoal)}
.nav ul{position:absolute;right:54px;top:10px;list-style:none;display:flex;gap:6px;font-size:10px;color:#b5b5b5}
.nav .is-current{color:var(--cyan)}
.brand-mark{border-radius:50%;background:linear-gradient(135deg,#4b6fd0,#2a3f9e)}
.hero .brand-mark{left:30px;top:50px;width:110px;height:110px}
.hero-title{left:0;width:583px;top:126px;font-size:42px}
.hero-title,.hero-sub,.hero-lead{padding-left:10px}
.hero-sub{left:0;width:583px;top:177px;font-size:20px;color:var(--cyan)}
.hero-lead{left:0;width:583px;top:214px;font-family:"Raleway",sans-serif;font-style:italic;font-weight:300;font-size:16.5px;line-height:1.35;color:#e6e6e6}

/* service rows */
.services{left:600px;top:18px;width:576px;height:322px;background:var(--yellow)}
.why{left:17px;top:340px;width:583px;height:320px;background:var(--teal)}
.section-title{font-size:25px}
.intro{font-size:9.5px;line-height:1.3}
.feature{position:absolute;width:130px;text-align:center}
.feature .icon{display:block;width:86px;height:86px;border-radius:50%;margin:0 auto}
.services .icon{background:linear-gradient(90deg,#ffffff 0%,#cfe7e4 15%,var(--teal) 60%)}
.why .icon{background:linear-gradient(90deg,#ffffff 0%,#fbeaa8 20%,var(--yellow) 60%)}
.feature h3{font-family:var(--display);font-weight:300;font-size:14px;letter-spacing:.5px}
.services .feature h3{margin-top:9px}
.why .feature h3{margin-top:20px}
.feature p{font-size:9px;line-height:1.35;margin:6px 8px 0}
.services .feature h3{color:var(--teal)}
.services .feature p,.services .intro{color:var(--ink)}
.chevron{width:22px;height:36px}

/* contact */
.contact{left:600px;top:340px;width:576px;height:320px;background:var(--salmon)}
.address{font-size:9px;line-height:1.3;color:#e88786}
.field{position:absolute;background:var(--charcoal);color:#9c9c9c;font-size:9px;padding:5px 18px}
.field-icon{position:absolute;width:19px;height:19px;border-radius:50%;background:linear-gradient(90deg,#fff,var(--charcoal) 70%);border:2px solid var(--charcoal)}
.pill{position:absolute;border-radius:10px;background:var(--sky);color:var(--white);font-family:var(--display);font-weight:300;font-size:10px;text-align:center;line-height:17px;letter-spacing:.3px}
.social-text{font-size:7px;color:#e88786}
.social-dot{left:224px;top:268px;width:30px;height:30px;border-radius:50%;background:radial-gradient(circle at 40% 40%,#7fe4ff,var(--sky));font-size:6px;line-height:30px;text-align:center;color:var(--white)}

/* plans */
.plans{left:17px;top:660px;width:583px;height:320px;background:var(--royal)}
.plan{position:absolute;top:102px;width:125px;height:175px;border-radius:10px;background:var(--charcoal);text-align:center}
.plan h3{font-family:var(--display);font-weight:300;font-size:16px;color:var(--grey);margin-top:6px;letter-spacing:.5px}
.plan p{font-size:9px;line-height:1.35;color:#c8c8c8;margin:12px 6px 0}
.plan .icon{position:absolute;left:19px;top:80px;width:86px;height:86px;border-radius:50%;background:linear-gradient(90deg,#ffffff 0%,#a9b7e6 25%,#2d43a8 70%)}
.plan.is-featured{background:var(--card-grey);border:1px solid #b0b0b0}
.plan.is-featured h3,.plan.is-featured p{color:var(--white)}

/* footer */
.footer{left:600px;top:660px;width:576px;height:320px;background:var(--charcoal)}
.footer .brand-mark{left:28px;top:58px;width:120px;height:120px}
.footer-title{left:160px;width:270px;top:104px;font-size:42px}
.tagline{left:160px;width:270px;top:156px;font-size:11px;color:#777}
.footer-note{left:100px;width:390px;top:180px;font-size:9.5px;line-height:1.3}
.footer-social{left:226px;top:219px;display:flex;gap:18px}
.footer-social span{width:20px;height:20px;border-radius:50%;background:radial-gradient(circle at 40% 40%,#8fe8ff,var(--sky))}
.footer-social span.is-light{background:var(--white)}
.pager{left:266px;top:247px;display:flex;gap:9px}
.pager span{width:8px;height:8px;background:linear-gradient(90deg,#eee,#666)}
</style>
</head>
<body>
<main class="canvas">

  <header class="panel hero">
    <nav class="abs nav"><ul><li class="is-current">Home</li><li>About</li><li>Work</li><li>Services</li><li>Team</li><li>Contact</li></ul></nav>
    <div class="abs brand-mark" aria-hidden="true"></div>
    <h1 class="abs display center hero-title">RANK LOFT</h1>
    <p class="abs display center hero-sub">FINALLY, SEO SERVICES THAT ACTUALLY WORK</p>
    <p class="abs center hero-lead">Top-notch SEO services that are guaranteed to boost your<br>search engine rankings! 100% Searchly-friendly.</p>
  </header>

  <section class="panel services">
    <h2 class="abs display center section-title" style="left:0;width:576px;top:34px">INDIVIDUAL SEO SERVICES</h2>
    <p class="abs center intro" style="left:0;width:576px;top:66px">Fusce dapibus, tellus ac cursus commodo, tortor mauris condimentum.<br>Duis mollis, est non commodo luctus, nisi erat porttitor ligula, eget lacinia odio sem nec elit.</p>
    <svg class="abs chevron" style="left:25px;top:142px" viewBox="0 0 22 36" aria-hidden="true"><polyline points="18,3 4,18 18,33" fill="none" stroke="var(--chevron)" stroke-width="4"/></svg>
    <svg class="abs chevron" style="left:545px;top:142px" viewBox="0 0 22 36" aria-hidden="true"><polyline points="4,3 18,18 4,33" fill="none" stroke="var(--chevron)" stroke-width="4"/></svg>
    <div class="feature" style="left:87px;top:118px"><span class="icon" role="img" aria-label="Branding icon"></span><h3>BRANDING</h3><p>Lorem ipsum dolor sit amet, consectetuer adipiscing elit, sed diam nonummy nibh.</p></div>
    <div class="feature" style="left:232px;top:118px"><span class="icon" role="img" aria-label="Design icon"></span><h3>DESIGN</h3><p>Sed ut perspiciatis unde omnis iste natus error sit voluptatem</p></div>
    <div class="feature" style="left:376px;top:118px"><span class="icon" role="img" aria-label="Development icon"></span><h3>DEVELOPMENT</h3><p>At vero eos et accusamus iusto odio dignissimos qui blanditis praesentium</p></div>
  </section>

  <section class="panel why">
    <p class="abs display center" style="left:0;width:583px;top:15px;font-size:10px;color:var(--yellow)">WHY CHOOSE?</p>
    <h2 class="abs display center section-title" style="left:0;width:583px;top:31px;font-size:21px">RANK LOFT</h2>
    <p class="abs center intro" style="left:0;width:583px;top:61px">Fusce dapibus, tellus ac cursus commodo, tortor mauris condimentum.<br>Quis mollis, est non commodo luctus, nisi erat porttitor ligula, eget lacinia odio sem nec elit</p>
    <div class="feature" style="left:78px;top:105px"><span class="icon" role="img" aria-label="Branding icon"></span><h3>BRANDING</h3><p>Lorem ipsum dolor sit amet, consectetuer adipiscing elit, sed diam nonummy nibh.</p></div>
    <div class="feature" style="left:222px;top:105px"><span class="icon" role="img" aria-label="Design icon"></span><h3>DESIGN</h3><p>Sed ut perspiciatis unde omnis iste natus error sit voluptatem</p></div>
    <div class="feature" style="left:366px;top:105px"><span class="icon" role="img" aria-label="Development icon"></span><h3>DEVELOPMENT</h3><p>At vero eos et accusamus iusto odio dignissimos qui blanditis praesentium</p></div>
  </section>

  <section class="panel contact">
    <h2 class="abs display center section-title" style="left:0;width:576px;top:28px;font-size:23px">GET IN TOUCH</h2>
    <p class="abs center address" style="left:0;width:596px;top:56px">418 Harbor Lane NW, Fairbridge DC 20417<br>Unitedland, Tel (202) 555-0147</p>
    <span class="field-icon" style="left:90px;top:120px"></span>
    <div class="field" style="left:117px;top:119px;width:130px;height:24px">YOUR NAME</div>
    <span class="field-icon" style="left:90px;top:154px"></span>
    <div class="field" style="left:117px;top:153px;width:130px;height:24px">YOUR EMAIL</div>
    <span class="field-icon" style="left:90px;top:188px"></span>
    <div class="field" style="left:117px;top:187px;width:130px;height:24px">YOUR #</div>
    <span class="field-icon" style="left:256px;top:128px"></span>
    <div class="field" style="left:282px;top:129px;width:178px;height:84px;padding:4px 12px">YOUR MESSAGE</div>
    <div class="pill" style="left:430px;top:241px;width:70px">SEND MESSAGE</div>
    <div class="abs social-dot">Follow</div>
    <span class="abs social-text" style="left:272px;top:280px">Share</span>
    <span class="abs social-text" style="left:306px;top:280px">Post</span>
    <span class="abs social-text" style="left:348px;top:280px">Blog</span>
  </section>

  <section class="panel plans">
    <h2 class="abs display center section-title" style="left:0;width:583px;top:34px;font-size:23px">SELECT A BOOSTER PLAN</h2>
    <p class="abs center intro" style="left:0;width:583px;top:63px">Neque porro quisquam est, qui dolorem ipsum quia dolor sit amet</p>
    <article class="plan" style="left:6px"><h3>PERSONAL</h3><p>Sed ut perspiciatis unde omnis iste natus error sit voluptatem</p><span class="icon" role="img" aria-label="Personal plan icon"></span></article>
    <article class="plan" style="left:153px"><h3>PROFESSIONAL</h3><p>At vero eos et accusamus iusto odio dignissimos qui blanditis praesentium</p><span class="icon" role="img" aria-label="Professional plan icon"></span></article>
    <article class="plan is-featured" style="left:296px"><h3>BUSINESS</h3><p>Sed ut perspiciatis unde omnis iste natus error sit voluptatem</p><span class="icon" role="img" aria-label="Business plan icon"></span></article>
    <article class="plan" style="left:440px"><h3>ENTERPRISE</h3><p>Lorem ipsum dolor sit amet, consectetuer adipiscing elit, sed diam nonummy nibh.</p><span class="icon" role="img" aria-label="Enterprise plan icon"></span></article>
    <p class="abs" style="left:237px;top:295px;font-size:9px;color:#b8c2e6">Duis mollis est non commodo luctus nisi erat porttitor.</p>
    <div class="pill" style="left:476px;top:291px;width:70px">GET STARTED</div>
  </section>

  <footer class="panel footer">
    <div class="abs brand-mark" aria-hidden="true"></div>
    <h2 class="abs display center footer-title">RANK LOFT</h2>
    <p class="abs center tagline">Where you can find me</p>
    <p class="abs center footer-note">Fusce dapibus, tellus ac cursus commodo, tortor mauris condimentum.<br>Duis mollis, est non commodo luctus, nisi erat porttitor ligula.</p>
    <div class="abs footer-social" aria-label="Social links"><span></span><span></span><span class="is-light"></span><span></span></div>
    <div class="abs pager" aria-hidden="true"><span></span><span></span><span></span><span></span></div>
  </footer>

</main>
</body>
</html>
```